Northern Horizons Published Photographer Website

I need a website to feature a home page slide show of 6 of my top photos then a few simple pages including; gallery, bio, social, checkout, services

Target Market(s)

photography

Industry/Entity Type

Photographer

Coding

Coded - Design and coding required

Number of Pages Required

5+ page

Colors

Designer to choose colors to be used in the design.

Requirements
Must have
• clean eye catching elegant trendy
Nice to have
• unique and creative from other photographer websites

```html
<!DOCTYPE html>
<html lang="en">
<head>
<meta charset="utf-8">
<title>Maren Holloway Photography</title>
<link href="https://fonts.googleapis.com/css2?family=Lato:wght@300;400;700&family=Dancing+Script:wght@400;700&display=swap" rel="stylesheet">
<style>
:root{
  --ink:#ffffff;
  --muted:#c9c9c9;
  --accent:#e8641f;
  --send:#f26b21;
  --green:#4caf50;
  --bg-dark:#111111;
  --bg-mid:#1b1b1b;
  --bg-black:#050505;
  --field:#1e1e1e;
  --field-line:#3a3a3a;
  --ghost:#0a0a0a;
}
*{margin:0;padding:0;box-sizing:border-box}
html,body{width:1200px;height:3398px;overflow:hidden;background:#000}
body{font-family:'Lato',sans-serif;color:var(--ink)}
.page{position:relative;width:1200px;height:3398px;overflow:hidden}
.abs{position:absolute}
section{position:absolute;left:0;width:1200px;overflow:hidden}

.nav a{position:absolute;top:34px;font-size:11px;letter-spacing:.5px;color:var(--ink);text-decoration:none;text-transform:uppercase}
.nav a.active{color:var(--accent)}
.nav a.active::before{content:"";position:absolute;left:0;right:0;top:-6px;height:2px;background:var(--accent)}
.brand{position:absolute;left:0;width:1200px;text-align:center;font-family:'Lato',sans-serif;font-weight:300;font-size:20px;letter-spacing:3px;color:var(--ink);text-transform:uppercase}

.hero{top:0;height:613px;background:linear-gradient(180deg,#1c1a2e 0%,#2f3a66 18%,#5a4a6e 32%,#8a4a35 45%,#b0502a 55%,#6b2f20 72%,#2a1a14 100%)}
.hero-title{position:absolute;top:280px;width:1200px;text-align:center;font-family:'Dancing Script',cursive;font-size:68px;line-height:1}
.hero-sub{position:absolute;top:355px;width:1200px;text-align:center;font-weight:300;font-size:48px;letter-spacing:2px}
.slider{position:absolute;top:572px;left:496px;width:210px;height:12px}

.kicker{position:absolute;width:1200px;text-align:center;font-family:'Dancing Script',cursive;font-size:26px;color:var(--muted)}
.heading{position:absolute;width:1200px;text-align:center;font-weight:300;font-size:34px;letter-spacing:6px;color:var(--accent);text-transform:uppercase}
.ghost{position:absolute;font-family:'Dancing Script',cursive;font-size:170px;color:var(--ghost);white-space:nowrap;line-height:1}

.btn{position:absolute;background:var(--green);color:#fff;font-size:12px;text-transform:uppercase;display:flex;align-items:center;justify-content:center;gap:6px;border-radius:2px}

.about{top:613px;height:350px;background:linear-gradient(90deg,#150f0e 0%,#2a1614 30%,#231514 60%,#150f0f 100%)}
.portrait{position:absolute;left:0;top:0;width:250px;height:350px;background:linear-gradient(180deg,#5a4a3a 0%,#3d3d42 55%,#5b5b60 100%)}
.about p{position:absolute;left:250px;width:700px;text-align:center;font-size:11px;color:var(--muted);line-height:19px}

.services{top:963px;height:626px;background:linear-gradient(135deg,#151515,#222)}
.tile{position:absolute}
.tile span{position:absolute;left:20px;bottom:10px;font-family:'Dancing Script',cursive;font-weight:700;font-size:27px;color:#fff}

.gallery{top:1589px;height:593px;background:var(--bg-black)}
.social{top:2182px;height:647px;background:var(--bg-mid)}
.contact{top:2829px;height:402px;background:linear-gradient(90deg,#2a2a2a 0%,#141414 25%,#0d0d0d 100%)}
.field{position:absolute;background:var(--field);border:1px solid var(--field-line);border-radius:2px;font-size:10px;color:#aaa;padding:10px 16px}
.send{position:absolute;left:520px;top:3138px;width:160px;height:37px;background:var(--send);border-radius:2px;display:flex;align-items:center;justify-content:center;gap:6px;font-size:12px;text-transform:uppercase}

.footer{top:3231px;height:167px;background:#080808}
.footer .label{position:absolute;font-size:11px;letter-spacing:.5px;color:var(--muted)}
.footer .label b{color:#fff;font-weight:700}
.footer-links a{position:absolute;top:145px;font-size:10px;color:#cfcfcf;text-decoration:none;text-transform:uppercase}
.dot{position:absolute;width:8px;height:8px;border-radius:50%;background:#fff}
</style>
</head>
<body>
<div class="page">

  <section class="hero" role="img" aria-label="Canyon at sunset with red rock cliffs under a purple sky">
    <nav class="nav">
      <a class="active" style="left:113px">Home</a>
      <a style="left:210px">About</a>
      <a style="left:310px">Services</a>
      <a style="left:842px">Gallery</a>
      <a style="left:933px">Checkout</a>
      <a style="left:1038px">Conatct</a>
    </nav>
    <div class="brand" style="top:28px">Maren Holloway</div>
    <div class="hero-title">Maren Holloway</div>
    <div class="hero-sub">PHOTOGRAPHY</div>
    <svg class="slider" viewBox="0 0 210 12">
      <circle cx="5" cy="6" r="3" fill="#e8641f"/>
      <circle cx="18" cy="6" r="3" fill="#e8641f"/>
      <line x1="32" y1="6" x2="62" y2="6" stroke="#aaa" stroke-width="1"/>
      <circle cx="72" cy="6" r="3.5" fill="none" stroke="#bbb"/>
      <circle cx="86" cy="6" r="3.5" fill="none" stroke="#bbb"/>
      <circle cx="104" cy="6" r="5" fill="#e8641f"/>
      <circle cx="120" cy="6" r="3.5" fill="none" stroke="#bbb"/>
      <circle cx="134" cy="6" r="3.5" fill="none" stroke="#bbb"/>
      <line x1="146" y1="6" x2="176" y2="6" stroke="#aaa" stroke-width="1"/>
      <circle cx="188" cy="6" r="3" fill="#e8641f"/>
      <circle cx="201" cy="6" r="3" fill="#e8641f"/>
    </svg>
  </section>

  <section class="about">
    <div class="ghost" style="left:1050px;top:325px;transform:rotate(-90deg);transform-origin:0 0;color:#0d0808;font-size:140px">About</div>
    <div class="portrait" role="img" aria-label="Portrait of the photographer"></div>
    <div class="kicker" style="top:48px">About</div>
    <div class="heading" style="top:82px;letter-spacing:0;font-size:33px">Get to know me</div>
    <p style="top:144px;color:#fff;font-weight:700">Hey, I'm Maren Holloway,</p>
    <p style="top:166px;font-size:12px;color:#ddd">I'm a trend setter, an adventurer, a coffee lover and a photographer!</p>
    <p style="top:191px;font-size:10px">Lorem ipsum dolor met, conctetur adipiscing elit. Integer massa magna, laoreet nec feugiat sed, elementum eget sem. Fusce mauris, aliquet in magna eu. elementum accumsan turpis. Cras mollis metus non nisi semper porta. Cras efficitur, ligula vel pharetra aliquet, mauris velit pretium ante lorem ipsum sit amet facilisis nisl felis pellentesque leo. Lorem ipsum, ligula vel pharetra aliquet, mauris velit pretium ante, eu facilisis nisl felis.</p>
    <div class="btn" style="left:542px;top:264px;width:116px;height:32px">Contact me</div>
  </section>

  <section class="services">
    <div class="ghost" style="left:150px;top:40px;transform:rotate(90deg);transform-origin:0 0;font-size:170px">Services</div>
    <div class="kicker" style="top:50px">Photography</div>
    <div class="heading" style="top:82px">Services</div>
    <div class="tile" role="img" aria-label="Waterfall beneath an arched bridge in autumn woods" style="left:210px;top:146px;width:388px;height:223px;background:linear-gradient(135deg,#4e7a2e,#b9c4c8 50%,#7a6a3a)"><span>Nature</span></div>
    <div class="tile" role="img" aria-label="Glass ball on a purple beach at sunset" style="left:602px;top:146px;width:387px;height:223px;background:linear-gradient(180deg,#7a4fc0,#b080d8 45%,#5a3aa0)"><span>Landscape</span></div>
    <div class="tile" role="img" aria-label="Bighorn sheep in desert scrub" style="left:210px;top:373px;width:258px;height:196px;background:linear-gradient(180deg,#9cc4e4,#b07a5a 45%,#8a7a6a)"><span>Wildlife</span></div>
    <div class="tile" role="img" aria-label="Orange sunset over a pier" style="left:472px;top:373px;width:256px;height:196px;background:linear-gradient(180deg,#c85a10,#f0a020 45%,#7a3a08)"><span>Sunsets</span></div>
    <div class="tile" role="img" aria-label="Sunrise through a rock arch with a glass ball" style="left:732px;top:373px;width:257px;height:196px;background:linear-gradient(180deg,#c05a30,#8ab4d8 40%,#b46a40)"><span>Sunrises</span></div>
  </section>

  <section class="gallery">
    <div class="ghost" style="left:1060px;top:560px;transform:rotate(-90deg);transform-origin:0 0;color:#161616;font-size:130px">Photography</div>
    <div class="kicker" style="top:50px">Photography</div>
    <div class="heading" style="top:84px">Gallery</div>
    <div class="abs" role="img" aria-label="Lake with rocky shore under clouds" style="left:210px;top:148px;width:183px;height:153px;background:linear-gradient(180deg,#d0d6de,#8aa0b0 55%,#3a8a9a)"></div>
    <div class="abs" role="img" aria-label="Dog on a sunny beach" style="left:409px;top:148px;width:183px;height:153px;background:linear-gradient(180deg,#3a6ab0,#8ab0d8 40%,#c8b090)"></div>
    <div class="abs" role="img" aria-label="Golden sunset over blue mountain ridges" style="left:608px;top:148px;width:381px;height:170px;background:linear-gradient(180deg,#5a5a60,#f0b020 35%,#3a4a6a 70%,#1a2230)"></div>
    <div class="abs" role="img" aria-label="Desert road under dramatic sky" style="left:210px;top:317px;width:382px;height:168px;background:linear-gradient(180deg,#2a5a8a,#b07a8a 35%,#7a3a20 60%,#3a2010)"></div>
    <div class="abs" role="img" aria-label="Elk in a green meadow" style="left:608px;top:334px;width:183px;height:151px;background:linear-gradient(180deg,#8ab040,#6a9030)"></div>
    <div class="abs" role="img" aria-label="Waterfall in autumn forest" style="left:806px;top:334px;width:183px;height:151px;background:linear-gradient(135deg,#7a8a40,#d8d8d0 55%,#5a6a30)"></div>
    <div class="btn" style="left:549px;top:506px;width:102px;height:32px">View all</div>
  </section>

  <section class="social">
    <div class="ghost" style="left:150px;top:30px;transform:rotate(90deg);transform-origin:0 0;color:#0c0c0c;font-size:150px">Photo Feed</div>
    <div class="kicker" style="top:50px">Photo Feed</div>
    <div class="heading" style="top:84px;letter-spacing:12px">Social</div>
    <div class="abs" role="img" aria-label="Stacked rock cairn in the desert" style="left:210px;top:160px;width:187px;height:186px;background:linear-gradient(180deg,#3a6ab0,#a0c0e0 40%,#8a4a30)"></div>
    <div class="abs" role="img" aria-label="Glass ball resting on sand" style="left:407px;top:160px;width:187px;height:186px;background:linear-gradient(180deg,#8a7a6a,#c8b8a0 50%,#6a5a48)"></div>
    <div class="abs" role="img" aria-label="Footbridge over a mountain stream" style="left:605px;top:160px;width:187px;height:186px;background:linear-gradient(180deg,#6a9ad0,#d0d8e0 35%,#5a6a4a)"></div>
    <div class="abs" role="img" aria-label="Seaside rocks at dusk" style="left:803px;top:160px;width:186px;height:186px;background:linear-gradient(180deg,#5a8ac0,#e8b090 40%,#4a8a9a)"></div>
    <div class="abs" role="img" aria-label="Green hills above a lake" style="left:210px;top:358px;width:187px;height:186px;background:linear-gradient(180deg,#8aa0c0,#d0d8e0 30%,#7a9a40 60%,#3a6a7a)"></div>
    <div class="abs" role="img" aria-label="Rock arch with sunburst" style="left:407px;top:358px;width:187px;height:186px;background:linear-gradient(180deg,#2a3a8a,#e0a080 45%,#2a2a30)"></div>
    <div class="abs" role="img" aria-label="Autumn forest path" style="left:605px;top:358px;width:187px;height:186px;background:linear-gradient(180deg,#6a9030,#d0b050 50%,#8a4a20)"></div>
    <div class="abs" role="img" aria-label="Rainbow over a prairie" style="left:803px;top:358px;width:186px;height:186px;background:linear-gradient(180deg,#5a5a60,#a0a0a8 45%,#8a7a50)"></div>
    <div class="btn" style="left:527px;top:564px;width:146px;height:29px">Follow us</div>
  </section>

  <section class="contact">
    <div class="abs" role="img" aria-label="Dark misty shoreline" style="left:0;top:120px;width:320px;height:282px;background:linear-gradient(180deg,#333,#1a1a1a)"></div>
    <div class="ghost" style="left:1075px;top:390px;transform:rotate(-90deg);transform-origin:0 0;color:#1c1c1c;font-size:100px">Get In Touch</div>
    <div class="kicker" style="top:50px">Get In Touch</div>
    <div class="heading" style="top:84px">Contact</div>
  </section>
  <div class="field" style="left:210px;top:2975px;width:241px;height:38px">Name</div>
  <div class="field" style="left:463px;top:2975px;width:257px;height:38px">Email</div>
  <div class="field" style="left:733px;top:2975px;width:256px;height:38px">Phone</div>
  <div class="field" style="left:210px;top:3026px;width:241px;height:37px">Address
    <svg class="abs" style="right:12px;top:11px" width="10" height="14" viewBox="0 0 10 14"><path d="M5 13C2 9 1 7 1 5a4 4 0 0 1 8 0c0 2-1 4-4 8z" fill="none" stroke="#999"/><circle cx="5" cy="5" r="1.5" fill="none" stroke="#999"/></svg>
  </div>
  <div class="field" style="left:210px;top:3076px;width:241px;height:39px">Choose Date &amp; Time
    <svg class="abs" style="right:12px;top:15px" width="10" height="6" viewBox="0 0 10 6"><path d="M1 1l4 4 4-4" fill="none" stroke="#999"/></svg>
  </div>
  <div class="field" style="left:463px;top:3026px;width:526px;height:89px">Your Message</div>
  <div class="send">
    <svg width="12" height="12" viewBox="0 0 12 12"><path d="M11 1L1 5l4 2 1 4z" fill="#fff"/></svg>Send now
  </div>

  <section class="footer">
    <div class="label" style="left:109px;top:38px;letter-spacing:3px;font-size:10px">NEWSLETTER</div>
    <div class="field" style="left:109px;top:59px;width:288px;height:25px;padding:5px 12px;font-style:italic;font-size:9px;background:#0d0d0d">Your email address...</div>
    <div class="brand" style="top:48px;font-size:18px">Maren Holloway</div>
    <div class="label" style="left:802px;top:38px">PHONE <b>123-456-7890</b></div>
    <div class="label" style="left:802px;top:74px;font-size:10px">EMAIL <b>info@marenholloway.com</b></div>
    <div class="label" style="left:989px;top:38px">FOLLOW US:</div>
    <span class="dot" style="left:990px;top:78px"></span>
    <span class="dot" style="left:1017px;top:78px"></span>
    <span class="dot" style="left:1048px;top:78px"></span>
    <span class="dot" style="left:1080px;top:78px"></span>
    <div class="abs" style="left:0;top:122px;width:1200px;height:1px;background:#222"></div>
    <nav class="footer-links">
      <a style="left:109px">Home</a>
      <a style="left:179px">About</a>
      <a style="left:252px">Services</a>
      <a style="left:336px">Gallery</a>
      <a style="left:418px">Checkout</a>
      <a style="left:512px">Social</a>
      <a style="left:586px">Conatct</a>
      <a style="left:794px">Copyright © 2019 Maren Holloway Photography.</a>
    </nav>
  </section>

</div>
</body>
</html>
```